Bakery Business Cards

We are in need of business cards for our bakery business--something non-generic that reflects our business and will stand out. We are a wholesale bakery that primarily services in-store bakeries, casinos, schools, distributors, and fund-raising companies. The family business was founded in 1960. (www.marlowsovenworks.com)

```html
<!DOCTYPE html>
<html lang="en">
<head>
<meta charset="utf-8">
<title>Marlow's Ovenworks — Business Cards</title>
<link href="https://fonts.googleapis.com/css2?family=Lato:wght@400;700;900&display=swap" rel="stylesheet">
<style>
  :root {
    --navy: #26449a;
    --navy-deep: #1f3a86;
    --card: #ececf0;
    --card-shade: #dfe1ea;
    --white: #ffffff;
  }
  * { box-sizing: border-box; margin: 0; padding: 0; }
  html, body { width: 1200px; height: 772px; overflow: hidden; }
  body {
    background: var(--navy-deep);
    font-family: "Lato", sans-serif;
    position: relative;
  }
  .card {
    position: absolute;
    top: 243px;
    width: 500px;
    height: 286px;
    border-radius: 4px;
    overflow: hidden;
    box-shadow: 0 10px 24px rgba(0, 0, 0, 0.3);
  }
  .card--front { left: 70px; }
  .card--back { left: 630px; }
  .card__pattern {
    position: absolute;
    inset: 0;
    background: radial-gradient(circle at 40% 40%, var(--card) 0%, var(--card-shade) 100%);
  }
  /* Front */
  .front__rule {
    position: absolute;
    left: 0; right: 0;
    height: 3px;
    background: var(--navy);
  }
  .front__rule--top { top: 96px; }
  .front__rule--bottom { top: 186px; }
  .front__panel {
    position: absolute;
    left: 140px; top: 72px;
    width: 220px; height: 140px;
    background: var(--navy);
    color: var(--white);
    display: flex;
    flex-direction: column;
    align-items: center;
    justify-content: center;
    text-align: center;
  }
  .brand__name {
    font-weight: 900;
    font-size: 26px;
    line-height: 1.05;
    letter-spacing: 0.5px;
  }
  .brand__since {
    font-weight: 400;
    font-size: 12px;
    letter-spacing: 1px;
    margin-top: 4px;
  }
  .front__url {
    font-weight: 700;
    font-size: 11px;
    letter-spacing: 1.5px;
    margin-top: 12px;
  }
  /* Back */
  .back__band {
    position: absolute;
    left: 0; top: 72px;
    width: 330px; height: 92px;
    background: var(--navy);
    color: var(--white);
    padding: 12px 16px 0 52px;
  }
  .back__icons {
    position: absolute;
    left: 16px; top: 14px;
    display: flex;
    flex-direction: column;
    gap: 6px;
  }
  .icon {
    width: 18px; height: 18px;
    background: var(--white);
    display: flex; align-items: center; justify-content: center;
  }
  .icon svg { width: 13px; height: 13px; fill: var(--navy); }
  .contact__phone {
    font-size: 24px;
    font-weight: 700;
    line-height: 1.1;
  }
  .contact__line {
    font-size: 10.5px;
    margin-top: 6px;
  }
  .back__brand {
    position: absolute;
    right: 22px; bottom: 40px;
    color: var(--navy);
    text-align: center;
  }
</style>
</head>
<body>
  <section class="card card--front">
    <div class="card__pattern" role="img" aria-label="Repeating pattern of small line-drawn baked goods"></div>
    <div class="front__rule front__rule--top"></div>
    <div class="front__rule front__rule--bottom"></div>
    <div class="front__panel">
      <div class="brand__name">Marlow's<br>Ovenworks</div>
      <div class="brand__since">SINCE 1960</div>
      <div class="front__url">www.marlowsovenworks.com</div>
    </div>
  </section>

  <section class="card card--back">
    <div class="card__pattern" role="img" aria-label="Repeating pattern of small line-drawn baked goods"></div>
    <div class="back__band">
      <div class="back__icons">
        <span class="icon"><svg viewBox="0 0 24 24"><path d="M6.6 10.8a15 15 0 0 0 6.6 6.6l2.2-2.2c.3-.3.7-.4 1-.2 1.1.4 2.3.6 3.6.6.6 0 1 .4 1 1V20c0 .6-.4 1-1 1A17 17 0 0 1 3 4c0-.6.4-1 1-1h3.5c.6 0 1 .4 1 1 0 1.3.2 2.5.6 3.6.1.3 0 .7-.2 1z"/></svg></span>
        <span class="icon"><svg viewBox="0 0 24 24"><path d="M12 2a7 7 0 0 0-7 7c0 5.2 7 13 7 13s7-7.8 7-13a7 7 0 0 0-7-7zm0 9.5A2.5 2.5 0 1 1 12 6.5a2.5 2.5 0 0 1 0 5z"/></svg></span>
        <span class="icon"><svg viewBox="0 0 24 24"><path d="M3 5h18v14H3zm2 2v.5l7 5 7-5V7zm0 3v7h14v-7l-7 5z"/></svg></span>
      </div>
      <div class="contact__phone">(555) 214-0387</div>
      <div class="contact__line">1820 Millbrook Rd, Riverton, OK 73199</div>
      <div class="contact__line">sales@marlowsovenworks.com</div>
    </div>
    <div class="back__brand">
      <div class="brand__name">Marlow's<br>Ovenworks</div>
      <div class="brand__since">SINCE 1960</div>
    </div>
  </section>
</body>
</html>
```